Corvalla Sponsored Content Images

Image spec: 1.91:1 ratio (1200x627px)We require 6x variations of this image: See the excel attached for the copy.Each image should contain the ZEMBO logo, 2 headshots if posible, a designed background and a CTA button + the copy.Please make sure that all of the copy is clear and big enough to read so it can be read on mobile devices.

Target Market(s)

This is for Corvalla ads to Executives of mid-market companies

Font styles to use
Sans Serif

Colors

Designer to choose colors to be used in the design.

```html
<!DOCTYPE html>
<html lang="en">
<head>
<meta charset="utf-8">
<title>ZEMBO Munch &amp; Learn Webinar</title>
<link rel="stylesheet" href="https://fonts.googleapis.com/css2?family=Dosis:wght@500;600&family=Montserrat:wght@800&display=swap">
<style>
  :root {
    --navy: #0f3566;
    --text-navy: #1d3c6e;
    --bg-light: #f2f2f2;
    --bg-mid: #d9d9d9;
    --photo-main: #5b5e61;
    --photo-main-light: #76797c;
    --photo-second: #d6d3cf;
    --photo-second-dark: #b9b5b0;
    --frame: #e6e6e6;
    --button-top: #2b8de0;
    --button-bottom: #0b4f98;
    --button-edge: #c9ccd0;
    --white: #ffffff;
  }
  html, body {
    margin: 0;
    padding: 0;
    overflow: hidden;
    background: var(--white);
  }
  .ad {
    position: relative;
    width: 1200px;
    height: 627px;
    overflow: hidden;
    background: radial-gradient(ellipse at 30% 50%, var(--bg-light) 0%, var(--bg-mid) 100%);
    font-family: "Dosis", sans-serif;
  }
  .backdrop {
    position: absolute;
    inset: 0;
  }
  .brand {
    position: absolute;
    left: 46px;
    top: 42px;
    margin: 0;
    font-family: "Dosis", sans-serif;
    font-weight: 600;
    font-size: 92px;
    line-height: 1;
    letter-spacing: 2px;
    color: var(--navy);
  }
  .event-copy {
    position: absolute;
    left: 45px;
    top: 190px;
    margin: 0;
    font-family: "Dosis", sans-serif;
    font-weight: 500;
    font-size: 36px;
    line-height: 50px;
    color: var(--text-navy);
    white-space: nowrap;
  }
  .event-copy span { display: block; }
  .cta {
    position: absolute;
    left: 50px;
    top: 474px;
    width: 494px;
    height: 86px;
    box-sizing: border-box;
    padding: 6px;
    background: linear-gradient(180deg, var(--white), var(--button-edge));
    border-radius: 3px;
  }
  .cta a {
    display: flex;
    align-items: center;
    justify-content: center;
    width: 100%;
    height: 100%;
    background: linear-gradient(180deg, var(--button-top) 0%, var(--button-bottom) 100%);
    color: var(--white);
    text-decoration: none;
    font-family: "Montserrat", sans-serif;
    font-weight: 800;
    font-size: 39px;
    letter-spacing: 0.5px;
  }
</style>
</head>
<body>
<main class="ad">
  <svg class="backdrop" width="1200" height="627" viewBox="0 0 1200 627" xmlns="http://www.w3.org/2000/svg">
    <defs>
      <linearGradient id="host-tone" x1="0" y1="0" x2="1" y2="1">
        <stop offset="0" stop-color="var(--photo-main-light)"/>
        <stop offset="1" stop-color="var(--photo-main)"/>
      </linearGradient>
      <linearGradient id="guest-tone" x1="0" y1="0" x2="0" y2="1">
        <stop offset="0" stop-color="var(--photo-second)"/>
        <stop offset="1" stop-color="var(--photo-second-dark)"/>
      </linearGradient>
    </defs>
    <polygon class="accent-top" points="372,0 648,0 510,140" fill="var(--navy)"/>
    <polygon class="accent-corner" points="1138,0 1200,0 1200,72" fill="var(--navy)"/>
    <polygon class="accent-right" points="1200,285 1200,605 1040,445" fill="var(--navy)"/>
    <polygon class="headshot-host" role="img" aria-label="Headshot of the first webinar host"
      points="805,-115 1168,250 805,612 442,250" fill="url(#host-tone)"
      stroke="url(#host-tone)" stroke-width="36" stroke-linejoin="round"/>
    <polygon class="headshot-frame" points="875,312 1092,528 875,744 658,528"
      fill="var(--frame)" stroke="var(--frame)" stroke-width="30" stroke-linejoin="round"/>
    <polygon class="headshot-guest" role="img" aria-label="Headshot of the second webinar host"
      points="875,338 1066,528 875,718 684,528" fill="url(#guest-tone)"
      stroke="url(#guest-tone)" stroke-width="20" stroke-linejoin="round"/>
  </svg>

  <h1 class="brand">ZEMBO</h1>

  <p class="event-copy">
    <span>Munch &amp; Learn Webinar:</span>
    <span>"Cybersecurity Starts at the Top"</span>
    <span>Your step-by step guide to</span>
    <span>implementing a cybersecurity strategy</span>
    <span>Wednesday, June 12th at 1pm EST</span>
  </p>

  <div class="cta"><a href="#">BOOK YOUR PLACE</a></div>
</main>
</body>
</html>
```